Develop a Corporate Identity for Telmo

Telmo is an Australian software start-up business which is targeted to Financial Services professionals. The software has functionality across all areas of financial planning, including customer relationship management, marketing, as well as modelling, document generation and compliance etc.

Our tagline: Powerful, Innovative, Intuitive. The tagline should not overlap the logo or other graphics.

I have attached a mock-up of the logo which I am very pleased with. I am not looking to change this substantially, but am leaving it open for any creative ideas. I am thinking that we might want to include a star on the top-left corner in to reference the Telmo star.

We are looking for the whole suite of Corporate Identity graphics:

- Logo (rectangular and square)
- Favicon
- Business card (template only, details to be filled in later. Include phone, email, address,
- Letterheads (A4, header and footer separated)
- Envelopes (C5)
- Cover page (full A4)
- With compliments slips

Extra points for business cards that stick out, I want people to be interested enough to keep and share them!

All graphics are to be provided in vector format (AI for example) as well as png with transparent background.

```html
<!DOCTYPE html>
<html lang="en">
<head>
<meta charset="utf-8">
<title>Telmo business card</title>
<link rel="stylesheet" href="https://fonts.googleapis.com/css2?family=Montserrat:wght@500&family=Open+Sans:wght@400&display=swap">
<style>
  :root {
    --page: #ffffff;
    --card-grey: #d3d3d3;
    --card-grey-light: #dedede;
    --brand-blue: #1d74c4;
    --sky: #2fb3e9;
    --sky-light: #63cfe6;
    --link-blue: #2aa7e0;
    --icon-dark: #1a66a8;
    --white: #ffffff;
    --pale: #cdeefa;
  }
  html, body { margin: 0; padding: 0; }
  body {
    width: 1200px; height: 899px; overflow: hidden;
    background: var(--page); position: relative;
    font-family: "Open Sans", Arial, sans-serif;
  }
  .card {
    position: absolute; overflow: hidden;
    box-shadow: 3px 4px 6px rgba(0,0,0,0.25);
  }
  .card-texture {
    position: absolute; inset: 0;
    background: linear-gradient(160deg, var(--card-grey-light), var(--card-grey));
  }
  .wordmark {
    position: absolute; margin: 0;
    font-family: "Montserrat", Arial, sans-serif; font-weight: 500;
    color: var(--brand-blue); line-height: 1; white-space: nowrap;
  }
  /* front */
  .card-front { left: 171px; top: 97px; width: 538px; height: 333px; }
  .card-front .wordmark {
    left: 0; right: 0; top: 108px; text-align: center;
    font-size: 112px; letter-spacing: 6px;
  }
  .card-front .site {
    position: absolute; left: 0; right: 0; top: 300px; text-align: center;
    font-size: 17px; color: var(--link-blue);
  }
  /* back */
  .card-back { left: 469px; top: 464px; width: 577px; height: 332px; }
  .card-back .shapes { position: absolute; inset: 0; }
  .card-back .wordmark { left: 36px; top: 38px; font-size: 58px; letter-spacing: 3px; }
  .holder-name {
    position: absolute; left: 384px; top: 50px; margin: 0;
    font-family: "Montserrat", Arial, sans-serif; font-weight: 500;
    font-size: 20px; letter-spacing: 1.5px; color: var(--white);
  }
  .holder-role {
    position: absolute; left: 452px; top: 74px; margin: 0;
    font-size: 9px; letter-spacing: 1px; color: var(--pale);
  }
  .contact {
    position: absolute; margin: 0; font-size: 15px; color: var(--white); white-space: nowrap;
  }
</style>
</head>
<body>
  <section class="card card-front">
    <div class="card-texture" role="img" aria-label="Light grey faceted triangle pattern"></div>
    <h1 class="wordmark">TELMO</h1>
    <p class="site" style="margin:0">telmo.com.au</p>
  </section>

  <section class="card card-back">
    <div class="card-texture" role="img" aria-label="Light grey faceted triangle pattern"></div>
    <svg class="shapes" width="577" height="332" viewBox="0 0 577 332">
      <polygon points="364,0 577,0 577,332 204,332" fill="var(--sky)"/>
      <polygon points="298,132 384,132 371,189 285,189" fill="var(--sky-light)"/>
      <polygon points="284,195 370,195 359,243 273,243" fill="var(--sky-light)"/>
      <polygon points="270,249 356,249 343,308 257,308" fill="var(--sky-light)"/>
      <line x1="285" y1="191" x2="517" y2="191" stroke="var(--sky-light)" stroke-width="3"/>
      <line x1="273" y1="245" x2="517" y2="245" stroke="var(--sky-light)" stroke-width="3"/>
      <!-- pin -->
      <path d="M330 138 a7 7 0 0 1 7 7 c0 6 -7 13 -7 13 c0 0 -7 -7 -7 -13 a7 7 0 0 1 7 -7z" fill="var(--icon-dark)"/>
      <circle cx="330" cy="145" r="2.6" fill="var(--sky-light)"/>
      <!-- phone -->
      <path d="M320 164 l5 -2 l3 6 l-3 2 c1 3 4 6 7 7 l2 -3 l6 3 l-2 5 c-9 0 -18 -9 -18 -18z" fill="var(--icon-dark)"/>
      <!-- mail -->
      <rect x="304" y="212" width="20" height="14" fill="var(--icon-dark)"/>
      <path d="M304 212 l10 8 l10 -8" fill="none" stroke="var(--sky-light)" stroke-width="1.5"/>
      <!-- wifi -->
      <g fill="none" stroke="var(--icon-dark)" stroke-width="2.2" stroke-linecap="round">
        <path d="M278 260 a16 16 0 0 1 22 0"/>
        <path d="M282 264 a10 10 0 0 1 14 0"/>
      </g>
      <circle cx="289" cy="268" r="2" fill="var(--icon-dark)"/>
      <!-- globe -->
      <g fill="none" stroke="var(--icon-dark)" stroke-width="1.6">
        <circle cx="284" cy="290" r="9"/>
        <ellipse cx="284" cy="290" rx="4" ry="9"/>
        <line x1="275" y1="290" x2="293" y2="290"/>
      </g>
    </svg>
    <h2 class="wordmark">TELMO</h2>
    <p class="holder-name">CORVINA</p>
    <p class="holder-role">CEO</p>
    <p class="contact" style="left:222px;top:140px;left:222px;margin-left:0"></p>
    <p class="contact" style="left:221px;top:140px"></p>
    <p class="contact" style="left:220px;top:0px"></p>
    <p class="contact" style="left:221px;top:0"></p>
    <p class="contact" style="left:222px;top:0"></p>
    <p class="contact" style="left:220px;top:0"></p>
    <p class="contact" style="left:220px;top:0"></p>
    <p class="contact" style="left:501px;top:0"></p>
    <p class="contact" style="left:222px;top:0"></p>
    <p class="contact" style="left:222px;top:0"></p>
    <p class="contact" style="left:222px;top:0"></p>
    <p class="contact" style="left:222px;top:0"></p>
    <p class="contact" style="left:222px;top:0"></p>
    <p class="contact" style="left:378px;top:140px">Melbourne, Australia</p>
    <p class="contact" style="left:369px;top:164px">+61-3-9000-4815</p>
    <p class="contact" style="left:348px;top:209px">telmo@mail.com</p>
    <p class="contact" style="left:330px;top:256px">corvina@telmo.com</p>
    <p class="contact" style="left:330px;top:282px">telmo.com.au</p>
  </section>
</body>
</html>
```